Molenvaart

2 homepage design for my tire webshop. One for the winter and one for the summer.
2 items have to come back.
1 a filterbox option to choose tire width, height and inch
2 an option where i can sell my tire mounting service
The customer can buy tires from me but also have the option to use only my skills for mounting their own tire.
My sellingpoint is my mobile service, a webshop with his own mechanic, and my good reputation.

```html
<!DOCTYPE html>
<html lang="en">
<head>
<meta charset="utf-8">
<title>Molenvaart – Tire Webshop Homepage</title>
<link href="https://fonts.googleapis.com/css2?family=Poppins:wght@500;600;700&family=Karla:ital,wght@0,400;0,700;1,400&display=swap" rel="stylesheet">
<style>
:root{
  --board:#4a4a4a;
  --blue:#12329a;
  --white:#ffffff;
  --ink:#1c1c1c;
  --body:#4d4d4d;
  --soft:#f4f4f4;
  --line:#cfcfcf;
  --black:#0b0b0b;
}
*{margin:0;padding:0;box-sizing:border-box}
html,body{width:696px;height:1200px;overflow:hidden;background:var(--board)}
body{font-family:"Karla",sans-serif;color:var(--body);position:relative}
.abs{position:absolute}
.panel{position:absolute;overflow:hidden;background:var(--white)}
.panel--mobile{left:9.5px;top:8.6px;width:329px;height:171.5px}
.panel--full{left:347.8px;top:8.6px;width:329px;height:1155px}
.sec{position:absolute;left:0;width:329px;overflow:hidden}
.heading{font-family:"Poppins",sans-serif;font-weight:600;text-transform:uppercase;color:var(--ink);font-size:8.6px;letter-spacing:.1px;white-space:nowrap}
.heading--center{left:0;width:100%;text-align:center}
.bar{position:absolute;height:1.5px;width:11.5px;background:var(--blue)}
.copy{font-size:3.9px;line-height:8.2px;text-align:justify}
.btn{position:absolute;height:12.4px;width:44.3px;border-radius:7px;font-family:"Poppins",sans-serif;font-weight:600;font-size:4.4px;display:flex;align-items:center;justify-content:center;text-transform:uppercase}
.btn--solid{background:var(--blue);color:var(--white)}
.btn--ghost{border:.8px solid var(--white);color:var(--white)}
.btn--outline{border:.8px solid var(--blue);color:var(--blue);background:var(--white)}
.btn--light{background:var(--white);color:var(--blue)}

/* hero */
.hero{top:0;height:171.5px}
.hero__photo{position:absolute;inset:0;background:
  radial-gradient(ellipse 45% 55% at 50% 45%,#3b3a36 0%,rgba(40,40,36,0) 70%),
  linear-gradient(180deg,#6b6c5d 0%,#4c4c43 35%,#2c2b28 70%,#1e1d1b 100%)}
.hero__shade{position:absolute;inset:0;background:rgba(0,0,0,.28)}
.logo{font-family:"Poppins",sans-serif;font-weight:500;font-size:8.6px;color:var(--white);letter-spacing:.1px;left:30px;top:5.5px}
.nav{right:32px;top:9px;display:flex;gap:5.2px;align-items:center;font-family:"Poppins",sans-serif;font-weight:600;font-size:3.3px;color:var(--white);text-transform:uppercase}
.hero__title{left:0;width:100%;top:56px;text-align:center;font-family:"Poppins",sans-serif;font-weight:700;font-size:10.6px;line-height:15px;color:var(--white);text-transform:uppercase;letter-spacing:-.15px}
.hero__text{left:0;width:100%;top:91px;text-align:center;font-size:3.9px;line-height:8.2px;color:#f1f1f1}
.dots{left:157px;top:163.3px;display:flex;gap:1.3px}
.dots span{width:2.2px;height:2.2px;border-radius:50%;background:var(--white)}
.dots span.on{background:var(--blue)}

/* about */
.about{top:171.5px;height:164px;background:var(--white)}
.photo{position:absolute}

/* products */
.products{top:335.5px;height:204px;background:var(--soft)}
.card{position:absolute;top:0;width:86px}
.card__img{position:absolute;left:0;top:44.3px;width:86px;height:79px;background:var(--white)}
.card__tire{position:absolute;left:50%;top:50%;width:64px;height:46px;transform:translate(-50%,-50%);border-radius:10px;background:radial-gradient(ellipse at 40% 40%,#3d3d3d 0%,#1a1a1a 55%,rgba(30,30,30,.15) 100%)}
.card__name{position:absolute;left:0;width:86px;top:127px;text-align:center;font-family:"Poppins",sans-serif;font-weight:600;font-size:4.5px;color:var(--ink)}
.filter{position:absolute;top:137.2px;width:20.5px;height:9px;border:.6px solid #9a9a9a;background:var(--white);font-size:3px;color:#666;display:flex;align-items:center;justify-content:space-between;padding:0 1.6px 0 4px}
.card__desc{position:absolute;left:0;width:86px;top:150.5px;text-align:center;font-size:3.8px;line-height:8.2px}
.arrow-lg{position:absolute;top:76px}

/* mounting */
.mounting{top:539.5px;height:152.5px}
.mounting__panel{position:absolute;left:0;top:0;width:166px;height:152.5px;background:var(--blue)}
.mounting__photo{position:absolute;left:166px;top:0;width:163px;height:152.5px;background:linear-gradient(110deg,#cfcfd2 0%,#7d7f85 22%,#2a2a2c 45%,#1a1a1b 70%,#3a3a3c 100%)}

/* testimonials */
.testimonials{top:692px;height:152.5px;background:var(--soft)}
.avatar{position:absolute;left:52.5px;top:47px;width:78px;height:78px;border-radius:50%;background:radial-gradient(circle at 50% 40%,#c9c3bb 0%,#9e9890 60%,#5a5550 100%)}
.quote{position:absolute;left:55px;top:46px;font-family:"Poppins",sans-serif;font-weight:700;font-size:22px;line-height:22px;color:#8e8e8e}
.testimonial__text{left:140.5px;top:53px;width:134px;font-style:italic;font-size:3.8px;line-height:8.3px;text-align:justify}
.testimonial__name{left:140.5px;top:104.5px;font-family:"Poppins",sans-serif;font-weight:600;font-size:4.5px;color:var(--blue)}
.testimonial__role{left:140.5px;top:111.5px;font-size:3.6px;color:#333}
.tbtn{position:absolute;top:112px;height:11px;display:flex;align-items:center;justify-content:center}

/* blogs */
.blogs{top:844.5px;height:164.5px;background:var(--white)}
.post{position:absolute;top:48px;width:86px}
.post__img{width:86px;height:57.6px}
.post__title{margin-top:4.6px;padding-left:2.4px;font-family:"Poppins",sans-serif;font-weight:600;font-size:4.4px;line-height:8.2px;color:var(--ink);text-transform:uppercase}
.post__text{padding-left:2.4px;font-size:3.8px;line-height:8.2px;color:#3d3d3d}

/* footer */
.footer{top:1009px;height:146px;background:radial-gradient(ellipse 60% 50% at 45% 60%,#1d1d1d 0%,var(--black) 70%)}
.footer__title{left:0;width:100%;top:15.5px;text-align:center;font-family:"Poppins",sans-serif;font-weight:700;font-size:8.6px;color:var(--white);text-transform:uppercase}
.signup{left:80px;top:39px;width:176px;height:14.3px;border-radius:8px;background:var(--white);border:.8px solid var(--white)}
.signup__field{position:absolute;left:13px;top:0;height:100%;display:flex;align-items:center;font-size:3.6px;color:#aaa}
.signup__btn{position:absolute;right:0;top:0;width:43.5px;height:100%;border-radius:7px;background:var(--blue);color:var(--white);font-family:"Poppins",sans-serif;font-weight:600;font-size:4.4px;display:flex;align-items:center;justify-content:center;text-transform:uppercase}
.rule{position:absolute;height:.5px;background:#5a5a5a}
.flogo{left:31.4px;top:80.5px;font-family:"Poppins",sans-serif;font-weight:500;font-size:8.6px;color:var(--white)}
.social{position:absolute;top:95.5px;width:8.8px;height:8.8px;border-radius:50%;background:var(--blue)}
.fcol{position:absolute;top:73px;color:var(--white)}
.fcol h4{font-family:"Poppins",sans-serif;font-weight:600;font-size:4.4px;text-transform:uppercase;margin-bottom:1.2px;white-space:nowrap}
.fcol li{list-style:none;font-size:3.8px;line-height:8.3px;white-space:nowrap;display:flex;align-items:center;gap:3px;padding-left:3px}
.copyright{left:0;width:100%;top:130px;text-align:center;font-size:3.8px;color:#ddd}
</style>
</head>
<body>

<!-- Winter / summer switch, first screen -->
<section class="panel panel--mobile">
  <div class="sec hero">
    <div class="hero__photo" role="img" aria-label="Row of winter tires standing on a misty tree-lined road"></div>
    <div class="hero__shade"></div>
    <div class="abs logo">MOLENVAART</div>
    <svg class="abs" style="left:295px;top:9.6px" width="4.5" height="3.8" viewBox="0 0 9 8"><rect y="0" width="9" height="1.4" fill="#fff"/><rect y="3.3" width="9" height="1.4" fill="#fff"/><rect y="6.6" width="9" height="1.4" fill="#fff"/></svg>
    <h1 class="abs hero__title">Lorem ipsum dolor sit amet conse<br>ctetur adipiscing elit sed.</h1>
    <p class="abs hero__text">Lorem ipsum dolor sit amet, consectetur adipiscing elit, sed do eiusmod tempor incididunt ut labore et dolore magna<br>aliqua. Quis ipsum suspendisse ultrices gravida Risus commodo viverra maecenas.</p>
    <a class="btn btn--ghost" style="left:119px;top:110.5px">Winter</a>
    <a class="btn btn--solid" style="left:166px;top:110.5px">Summer</a>
  </div>
</section>

<!-- Full homepage -->
<main class="panel panel--full">

  <section class="sec hero">
    <div class="hero__photo" role="img" aria-label="Row of tires standing on a misty tree-lined road"></div>
    <div class="hero__shade"></div>
    <div class="abs logo">MOLENVAART</div>
    <nav class="abs nav" style="right:30px">
      <span>Home</span><span>About us</span><span>Products</span><span>Services</span><span>Blog</span><span>Contact us</span>
      <svg width="3.4" height="3.4" viewBox="0 0 10 10"><circle cx="4" cy="4" r="3" fill="none" stroke="#fff" stroke-width="1.6"/><line x1="6.2" y1="6.2" x2="9.3" y2="9.3" stroke="#fff" stroke-width="1.8"/></svg>
      <svg width="3.8" height="3.4" viewBox="0 0 11 10"><path d="M0 1h2l1.5 5h6L11 2H3" fill="none" stroke="#fff" stroke-width="1.4"/><circle cx="4.3" cy="8.6" r="1" fill="#fff"/><circle cx="8.6" cy="8.6" r="1" fill="#fff"/></svg>
    </nav>
    <h1 class="abs hero__title">Lorem ipsum dolor sit amet conse<br>ctetur adipiscing elit sed.</h1>
    <p class="abs hero__text">Lorem ipsum dolor sit amet, consectetur adipiscing elit, sed do eiusmod tempor incididunt ut labore et dolore magna<br>aliqua. Quis ipsum suspendisse ultrices gravida Risus commodo viverra maecenas.</p>
    <a class="btn btn--solid" style="left:142.4px;top:110.5px">Get started</a>
    <div class="abs dots"><span></span><span class="on"></span><span></span><span></span><span></span></div>
  </section>

  <section class="sec about">
    <div class="photo" style="left:17.6px;top:24px;width:130.5px;height:123px;background:linear-gradient(120deg,#d8dadd 0%,#a9adb3 40%,#5d6c8a 65%,#2d2f33 100%)" role="img" aria-label="Mechanic in blue overalls handling a tire beside a car"></div>
    <h2 class="abs heading" style="left:164px;top:22px">About Molenvaart</h2>
    <div class="bar" style="left:164.3px;top:36.5px"></div>
    <p class="abs copy" style="left:164.3px;top:46px;width:134px">Sed ut perspiciatis unde omnis iste natus error sit voluptatem accusantium doloremque laudantium, totam rem aperiam, eaque ipsa quae ab illo inventore veritatis et quasi architecto beatae vitae dicta sunt explicabo. Nemo enim ipsam voluptatem quia voluptas sit aspernatur aut odit aut fugit, sed quia consequuntur magni dolores eos qui ratione voluptatem sequi nesciunt. Neque porro quisquam est, qui dolorem ipsum quia dolor sit amet, consectetur, adipisci velit, sed quia non numquam eius modi tempora incidunt ut labore et dolore magnam aliquam quaerat voluptatem. Ut enim ad minima veniam, quis nostrum exercitationem ullam corporis suscipit laboriosam, nisi ut aliquid ex ea commodi.</p>
    <a class="btn btn--solid" style="left:164.3px;top:132px">Learn more</a>
  </section>

  <section class="sec products">
    <h2 class="abs heading heading--center" style="top:21.5px">Our products</h2>
    <div class="bar" style="left:158.7px;top:35.5px"></div>
    <svg class="arrow-lg" style="left:11px" width="7" height="10" viewBox="0 0 7 10"><path d="M5.5 1 1.8 5l3.7 4" fill="none" stroke="#111" stroke-width="1.6"/></svg>
    <svg class="arrow-lg" style="left:311px" width="7" height="10" viewBox="0 0 7 10"><path d="M1.5 1 5.2 5 1.5 9" fill="none" stroke="#111" stroke-width="1.6"/></svg>

    <article class="card" style="left:25.7px">
      <div class="card__img"><div class="card__tire" role="img" aria-label="Stack of black tires"></div></div>
      <div class="card__name">PRODUCT NAME</div>
      <div class="filter" style="left:7.1px">width<span>▴▾</span></div>
      <div class="filter" style="left:32.9px">height<span>▴▾</span></div>
      <div class="filter" style="left:58.6px">inch<span>▴▾</span></div>
      <p class="card__desc">Lorem ipsum dolor sit amet, consectetur<br>adipiscing elit sed do eiusmod.</p>
      <a class="btn btn--outline" style="left:20.8px;top:168px">Shop now</a>
    </article>
    <article class="card" style="left:121px">
      <div class="card__img"><div class="card__tire" role="img" aria-label="Tire on alloy rim in front of a tire stack"></div></div>
      <div class="card__name">PRODUCT NAME</div>
      <div class="filter" style="left:7.1px">width<span>▴▾</span></div>
      <div class="filter" style="left:32.9px">height<span>▴▾</span></div>
      <div class="filter" style="left:58.6px">inch<span>▴▾</span></div>
      <p class="card__desc">Lorem ipsum dolor sit amet, consectetur<br>adipiscing elit sed do eiusmod.</p>
      <a class="btn btn--outline" style="left:20.8px;top:168px">Shop now</a>
    </article>
    <article class="card" style="left:216.8px">
      <div class="card__img"><div class="card__tire" role="img" aria-label="Pile of four black tires"></div></div>
      <div class="card__name">PRODUCT NAME</div>
      <div class="filter" style="left:7.1px">width<span>▴▾</span></div>
      <div class="filter" style="left:32.9px">height<span>▴▾</span></div>
      <div class="filter" style="left:58.6px">inch<span>▴▾</span></div>
      <p class="card__desc">Lorem ipsum dolor sit amet, consectetur<br>adipiscing elit sed do eiusmod.</p>
      <a class="btn btn--outline" style="left:20.8px;top:168px">Shop now</a>
    </article>
  </section>

  <section class="sec mounting">
    <div class="mounting__panel">
      <h2 class="abs heading" style="left:15.7px;top:21px;color:var(--white)">Mounting service</h2>
      <div class="bar" style="left:15.9px;top:35.5px;background:var(--white)"></div>
      <p class="abs copy" style="left:15.9px;top:44.5px;width:134.5px;color:#e6e9f5">Sed ut perspiciatis unde omnis iste natus error sit voluptatem accusantium doloremque laudantium, totam rem aperiam, eaque ipsa quae ab illo inventore veritatis et quasi architecto beatae vitae dicta sunt explicabo. Nemo enim ipsam voluptatem quia voluptas sit aspernatur aut odit aut fugit, sed quia consequuntur magni dolores eos qui ratione voluptatem sequi nesciunt. Neque porro quisquam est, qui dolorem ipsum quia dolor sit amet, consectetur, adipisci velit, sed quia non numquam eius modi tempora incidunt ut labore et dolore magnam aliquam.</p>
      <a class="btn btn--light" style="left:15.9px;top:114px">Learn more</a>
    </div>
    <div class="mounting__photo" role="img" aria-label="Racks of new tires lined up in a tire shop"></div>
  </section>

  <section class="sec testimonials">
    <h2 class="abs heading heading--center" style="top:21.5px">Our client testimonials</h2>
    <div class="bar" style="left:158.7px;top:35.5px"></div>
    <div class="avatar" role="img" aria-label="Portrait photo of a client in a suit"></div>
    <div class="quote">“</div>
    <p class="abs testimonial__text">Lorem ipsum dolor sit amet, consectetur adipiscing elit, sed do eiusmod tempor incididunt ut labore et dolore magna aliqua. Ut enim ad minim veniam, quis nostrud exercitation ullamco laboris nisi ut aliquip ex ea commodo consequat. Duis aute irure dolor in reprehenderit in voluptate velit esse cillum dolore eu fugiat nulla pariatur. Excepteur sint occaecat cupidatat non proident, sunt in culpa qui officia deserunt mollit anim id est laborum.</p>
    <div class="abs testimonial__name">JOHN DOE</div>
    <div class="abs testimonial__role">Lorem ipsum dolor sit amet</div>
    <div class="tbtn" style="left:245px;width:21.5px;background:var(--white);box-shadow:0 .5px 2px rgba(0,0,0,.12)"><svg width="5" height="3" viewBox="0 0 10 6"><path d="M10 3H1M3.5 .5 1 3l2.5 2.5" fill="none" stroke="#111" stroke-width="1.2"/></svg></div>
    <div class="tbtn" style="left:270px;width:8px"><svg width="5" height="3" viewBox="0 0 10 6"><path d="M0 3h9M6.5 .5 9 3 6.5 5.5" fill="none" stroke="#111" stroke-width="1.2"/></svg></div>
  </section>

  <section class="sec blogs">
    <h2 class="abs heading heading--center" style="top:25px">Our latest blogs</h2>
    <div class="bar" style="left:158.7px;top:39px"></div>
    <article class="post" style="left:30.5px">
      <div class="post__img" style="background:linear-gradient(120deg,#c5cad1 0%,#7e8a9e 50%,#3a4355 100%)" role="img" aria-label="Mechanic fitting a tire onto a car"></div>
      <h3 class="post__title">Lorem ipsum dolor sit amet,<br>consectetur adipiscing</h3>
      <p class="post__text">Lorem ipsum dolor sit amet, consectetur adip iscing elit, sed do eiusmod tempor incididunt ut labore et dolore magna aliqua.</p>
    </article>
    <article class="post" style="left:121.3px">
      <div class="post__img" style="background:radial-gradient(ellipse at 50% 45%,#2e2f22 0%,#6b7a2c 35%,#c7c25a 80%)" role="img" aria-label="Single tire standing on sunlit grass"></div>
      <h3 class="post__title">Lorem ipsum dolor sit amet,<br>consectetur adipiscing</h3>
      <p class="post__text">Lorem ipsum dolor sit amet, consectetur adip iscing elit, sed do eiusmod tempor incididunt ut labore et dolore magna aliqua.</p>
    </article>
    <article class="post" style="left:212px">
      <div class="post__img" style="background:linear-gradient(135deg,#c06a3a 0%,#4a3a33 35%,#2a2a2c 60%,#6e6e70 100%)" role="img" aria-label="Close-up of tire tread"></div>
      <h3 class="post__title">Lorem ipsum dolor sit amet,<br>consectetur adipiscing</h3>
      <p class="post__text">Lorem ipsum dolor sit amet, consectetur adip iscing elit, sed do eiusmod tempor incididunt ut labore et dolore magna aliqua.</p>
    </article>
  </section>

  <footer class="sec footer">
    <h2 class="abs footer__title">Join our mailing list</h2>
    <form class="abs signup">
      <span class="signup__field">Enter Email Here</span>
      <span class="signup__btn">Subscribe</span>
    </form>
    <div class="rule" style="left:30.5px;top:62.4px;width:268px"></div>
    <div class="abs flogo">MOLENVAART</div>
    <span class="social" style="left:31px"></span>
    <span class="social" style="left:44px"></span>
    <span class="social" style="left:57px"></span>
    <span class="social" style="left:70px"></span>

    <div class="fcol" style="left:100.5px">
      <h4>Quick links</h4>
      <ul><li>»&nbsp;Home</li><li>»&nbsp;Product</li><li>»&nbsp;Why Choose Us</li><li>»&nbsp;Benefits</li></ul>
    </div>
    <div class="fcol" style="left:160px">
      <h4>Legal</h4>
      <ul><li>»&nbsp;Privacy Policy</li><li>»&nbsp;Terms &amp; Conditions</li><li>»&nbsp;Contact Us</li><li>»&nbsp;About Us</li></ul>
    </div>
    <div class="fcol" style="left:224px">
      <h4>Contact us</h4>
      <ul>
        <li><svg width="3" height="4" viewBox="0 0 6 8"><path d="M3 8S0 4.6 0 3a3 3 0 0 1 6 0c0 1.6-3 5-3 5z" fill="#fff"/><circle cx="3" cy="3" r="1.1" fill="#000"/></svg>&nbsp;123 Sed ut perspiciatis unde omnis</li>
        <li style="padding-left:10px">iste natus error sit voluptatem</li>
        <li style="margin-top:2px"><svg width="3.5" height="3.5" viewBox="0 0 8 8"><path d="M1.6 0 3 2 2 3.2a5 5 0 0 0 2.8 2.8L6 5l2 1.4L7 8C3 8 0 5 0 1z" fill="#fff"/></svg>&nbsp;123 456 7890</li>
        <li style="margin-top:2px"><svg width="4" height="3" viewBox="0 0 8 6"><rect width="8" height="6" rx=".6" fill="#fff"/><path d="M0 .5 4 3.5 8 .5" fill="none" stroke="#000" stroke-width=".8"/></svg>&nbsp;info@molenvaart-banden.nl</li>
      </ul>
    </div>
    <div class="rule" style="left:20px;top:125px;width:288px"></div>
    <p class="abs copyright">© Copyright 2021 &nbsp;<b style="color:#fff">MOLENVAART</b>&nbsp; | &nbsp; All Rights Reserved</p>
  </footer>
</main>

</body>
</html>
```